Flyer Design Project -Dental Seminar Day Australia

This is to promote Dental Practice Seminars in Gold Coast, Sydney and Melbourne, Australia later this year.

The theme of the day is "Stand up, Step Up, Step Out!"

See attached files for more information.

The aim is to wow the dentists, so that they will want to go to this course. This flyer will be emailed, faxed, sent and hand delivered to dentists across Australia.

Target Market(s)

1. Dentists looking to start their own practice but are afraid. Age group 24-50.

Industry/Entity Type

Dental

Requirements
Must have
• flyer must be double sided, and use all the pictures attached.
registration section like file attached
at bottom to use logos of the sponsors listed in word. find their logos on the web.
Nice to have
• different, innovation, bring something to the dental field that they have never seen before. use diffrent fonts, colors etc. stand out!

```html
<!DOCTYPE html>
<html lang="en">
<head>
<meta charset="utf-8">
<title>Dental Practice Seminar Day – Flyer</title>
<link href="https://fonts.googleapis.com/css2?family=Source+Sans+3:wght@400;500;600;700&display=swap" rel="stylesheet">
<style>
  :root{
    --sky-top:#52c8f2;
    --sky-bottom:#d9f3fc;
    --navy:#17196b;
    --ink:#1d1d1d;
    --rule:#1d1d1d;
    --form-bg:#ffffff;
    --form-edge:#bfe8f8;
    --band:#d3f0fb;
    --footer:#7a7a7a;
    --chip:#5b5b5b;
    --photo:#c9b7a6;
  }
  *{box-sizing:border-box;margin:0;padding:0}
  html,body{width:848px;height:1200px;overflow:hidden;background:#fff}
  body{font-family:"Source Sans 3",Arial,sans-serif;color:var(--ink)}
  .flyer{position:relative;width:848px;height:1200px;overflow:hidden}

  .hero{position:absolute;left:0;top:0;width:848px;height:552px;
    background:linear-gradient(180deg,var(--sky-top) 0%,#8fdcf6 55%,var(--sky-bottom) 100%)}
  .venues-intro{position:absolute;left:12px;top:4px;width:400px;font-size:24px;line-height:27px;font-weight:500;color:var(--navy)}
  .venues{position:absolute;left:22px;top:76px;list-style:none;font-size:31px;line-height:39px;font-weight:500;color:var(--navy)}
  .times{position:absolute;left:14px;top:320px;font-size:23px;line-height:27px;font-weight:500;color:var(--navy)}

  .speaker-label{position:absolute;left:455px;top:4px;font-size:23px;color:var(--navy);font-weight:500}
  .speaker-name{position:absolute;left:462px;top:36px;font-size:28px;color:var(--navy);font-weight:500}
  .speaker-photo{position:absolute;left:681px;top:15px;width:133px;height:172px;
    background:linear-gradient(160deg,#e6e6e6 0%,var(--photo) 60%,#8d8478 100%)}
  .bio{position:absolute;left:420px;top:74px;width:396px;font-size:15.3px;line-height:19.6px;color:var(--ink)}
  .bio p.first{width:252px}
  .bio p + p{margin-top:20px}
  .bio .wide{margin-left:0}

  .reg-title{position:absolute;left:10px;top:508px;font-size:24px;font-weight:500;color:var(--navy)}

  .form{position:absolute;left:0;top:552px;width:848px;height:458px;background:var(--form-bg);
    border:2px solid var(--form-edge);border-left:none;border-right:none}
  .box{display:inline-block;width:21px;height:21px;border:1.5px solid var(--ink);background:#fff;vertical-align:middle}
  .option{position:absolute;left:8px}
  .option .head{font-size:19.5px;display:flex;align-items:center;gap:9px}
  .option .meta{margin-left:30px;font-size:13px;line-height:15px}
  .diet{position:absolute;left:8px;top:328px;font-size:14px;display:flex;align-items:center;gap:9px}
  .diet-line{position:absolute;left:20px;width:308px;border-bottom:1.5px solid var(--rule)}

  .field{position:absolute;left:380px;width:460px;height:20px;border-bottom:1.5px solid var(--rule);font-size:13.5px}
  .field span{position:absolute;top:2px}
  .pay{position:absolute;left:376px;top:217px;display:flex;align-items:center;font-size:15px}
  .pay .box{margin-right:7px}
  .fax-note{position:absolute;left:441px;top:351px;width:328px;height:22px;background:var(--chip);color:#fff;
    font-size:14.5px;text-align:center;line-height:22px}
  .cheque{position:absolute;left:376px;top:380px;font-size:13.5px;line-height:16px;display:flex;gap:9px}
  .cheque .addr{padding-left:178px}

  .sponsors{position:absolute;left:0;top:1010px;width:848px;height:127px;background:linear-gradient(180deg,#e8f8fd,var(--band))}
  .sponsors h2{position:absolute;left:8px;top:26px;font-size:24px;font-weight:500;color:var(--navy)}
  .sponsor-row{position:absolute;left:4px;top:64px;width:842px;height:60px;display:flex;align-items:center;justify-content:space-between;background:#fff;padding:0 6px}
  .sponsor{display:flex;align-items:center;gap:5px;font-size:13px;font-weight:700;color:var(--navy);white-space:nowrap}
  .sponsor i{display:inline-block;width:10px;height:10px;background:var(--navy)}

  .policy{position:absolute;left:0;top:1137px;width:848px;height:63px;background:var(--footer);color:#fff;
    font-size:10.4px;line-height:12.6px;padding:2px 4px}
  .policy b{font-weight:700}
</style>
</head>
<body>
<main class="flyer">
  <section class="hero">
    <p class="venues-intro">This unique, power-packed event will be held at the following venues:</p>
    <ul class="venues">
      <li>+ Sat July 21, 2012 –</li>
      <li>Seaview Hotel Gold Coast</li>
      <li>+ Fri August 17, 2012 –</li>
      <li>Parkside Hotel Sydney</li>
      <li>+ Fri Sep 21, 2012 –</li>
      <li>Seaview Hotel Melbourne</li>
    </ul>
    <p class="times">All days commence at 8.30am<br>and conclude at 5.00pm<br>6.5hrs CPD</p>

    <h2 class="speaker-label">About our speaker:</h2>
    <h1 class="speaker-name">Dr. Daniel Marsh</h1>
    <div class="speaker-photo" role="img" aria-label="Portrait photograph of the speaker"></div>
    <div class="bio">
      <p class="first">Daniel Marsh is regarded as one of Australia's most successful young dentists. He has co-founded two successful dental clinics in Brisbane, employing four dentists and numerous staff members. He is a</p>
      <p style="margin-top:0">leading provider of Mini Dental Implants and also lectures on their use. His interests lie in cosmetic, orthodontic and implant dentistry, but he is most passionate about starting up practice and creating patients who love you.</p>
      <p>Daniel has always displayed an enthusiasm and ability beyond his years. His passion for people has landed him many leading roles including School Captain, President of St Clement Society, Order of Australia for Community, President of the University Students Society to name a few. He regularly presents powerful, dynamic motivational talks to dentists and health professionals across Australia. He will share with you the secrets of how to start up and successfully grow your dental practice in a step-by-step, easy-to-follow manner. You will leave ready to take that next step.</p>
    </div>
    <h2 class="reg-title">Registration:</h2>
  </section>

  <section class="form">
    <div class="option" style="top:8px">
      <div class="head"><span class="box"></span>EARLY BIRD Registration - Dentist</div>
      <div class="meta">Cost - $315 GST inc.<br>Gold Coast Deadline - 21st June 2012<br>Sydney Deadline - 17th July 2012<br>Melbourne Deadline - 17th July 2012</div>
    </div>
    <div class="option" style="top:113px">
      <div class="head"><span class="box"></span>STANDARD Registration - Dentist</div>
      <div class="meta">Cost - $495 GST inc.<br>Gold Coast Deadline - 21st June 2012<br>Sydney Deadline - 17th July 2012<br>Melbourne Deadline - 17th July 2012</div>
    </div>
    <div class="option" style="top:215px">
      <div class="head"><span class="box"></span>STANDARD Registration - Student</div>
      <div class="meta">Cost - $110 GST inc.<br>Gold Coast Deadline - 21st June 2012<br>Sydney Deadline - 17th July 2012<br>Melbourne Deadline - 17th July 2012</div>
    </div>
    <div class="diet"><span class="box"></span>Special dietary requirements:</div>
    <div class="diet-line" style="top:374px"></div>
    <div class="diet-line" style="top:406px"></div>
    <div class="diet-line" style="top:439px"></div>

    <div class="field" style="top:8px"><span>Dentist:</span></div>
    <div class="field" style="top:43px"><span>Dental Auxiliary:</span></div>
    <div class="field" style="top:78px"><span>Address:</span></div>
    <div class="field" style="top:112px"></div>
    <div class="field" style="top:150px"><span>Suburb:</span><span style="left:196px">State:</span><span style="left:312px">P/Code:</span></div>
    <div class="field" style="top:185px"><span>Telephone: (&nbsp;&nbsp;&nbsp;&nbsp;&nbsp;&nbsp;&nbsp;)</span><span style="left:240px">Fax: (&nbsp;&nbsp;&nbsp;&nbsp;&nbsp;&nbsp;&nbsp;)</span></div>
    <div class="pay"><span class="box"></span>Please bill my credit card<span class="box" style="margin-left:18px"></span>Debit Card<span class="box" style="margin-left:18px"></span>Charge Card</div>
    <div class="field" style="top:250px"><span>Name on Card:</span></div>
    <div class="field" style="top:285px"><span>Card Number:</span></div>
    <div class="field" style="top:322px"><span>Expiry Date:</span><span style="left:164px">Signature:</span></div>
    <div class="fax-note">Fax completed registration form to (07) 3555 0142</div>
    <div class="cheque"><span class="box"></span>
      <div>I enclose a cheque payable to Elevare Seminars.<br>Please mail cheque &amp; form to: Elevare Seminars,
        <div class="addr">P.O Box 2480,<br>Westbrook Hills, QLD 4199</div></div>
    </div>
  </section>

  <section class="sponsors">
    <h2>Our Sponsors:</h2>
    <div class="sponsor-row">
      <span class="sponsor"><i></i>Fitout Studio</span>
      <span class="sponsor">Dental Store</span>
      <span class="sponsor">Clearvue</span>
      <span class="sponsor">Harlow Dental Supply</span>
      <span class="sponsor">Medica Finance</span>
      <span class="sponsor">Coastline Dental</span>
      <span class="sponsor">Northgate Capital</span>
    </div>
  </section>

  <footer class="policy"><b>Cancellation Policy:</b> Any registered participant whose cancellation is received in writing at least twenty (20) business days prior to a seminar for which the participant is registered for, will receive a refund of 75% of the registration fee paid. Any registered participant who cancels his or her registration within twenty (20) business days prior to a seminar for what the participant is registered for, will not receive a refund of the registration fee or any other costs incurred. The organisers reserve the right to cancel or postpone a seminar at any time with no responsibility to the participants other than a full refund of the registration fee.</footer>
</main>
</body>
</html>
```